Einladungskarten für Der Helle Bogen
Designer hat mehrere Vorschläge entwickelt und Änderungen super schnell umgesetzt. Wir waren sehr zufrieden und freuen uns auf unsere diesjährige Einladungskarte.
Zielgruppe
Wir sind ein Tochterunternehmen von Harting Verlag. Wir sind 'Der Helle Bogen' , Holding der Radio Stationen/Beteiligungen und möchten alle Geschäftsführer/innen der Beteiligungen, einige Politiker und Medienräte zu einem Event einladen.
Aufgabenstellung
Wir hätten gerne eine quadratische Karte.
Das Event heißt 'Ortsabend 2023'
Termin 03.07.2023 um 19 Uhr
Anmeldung bis spätestens 23.06.2022 an events@heller-bogen.de
Diese Karte gilt als Eintrittskarte
Adresse: KAIHALLE, Lindenweg 52, 90461 Nürnberg
Dresscode: Business Casual
Firmenfarben: Blau: RGB 23/110/182 und Grau: RGB 134/135/135
Firmenschriftart: Century Gothic

```html
<!DOCTYPE html>
<html lang="de">
<head>
<meta charset="utf-8">
<title>Ortsabend 2023 – Einladungskarte</title>
<link rel="stylesheet" href="https://fonts.googleapis.com/css2?family=Questrial&family=Ubuntu:wght@700&display=swap">
<style>
  :root {
    --brand-blue: #176eb6;
    --brand-grey: #868787;
    --board-bg: #c8c6c7;
    --ink: #1a1a1a;
    --paper: #ffffff;
    --fold: #d9d9d9;
  }
  * { margin: 0; padding: 0; box-sizing: border-box; }
  html, body { width: 1109px; height: 1200px; overflow: hidden; }
  body {
    position: relative;
    background: var(--board-bg);
    font-family: "Questrial", "Century Gothic", sans-serif;
    color: var(--ink);
  }
  .board-title {
    position: absolute; left: 58px;
    font-size: 33px; letter-spacing: 0.5px; font-weight: 400;
  }
  .board-title--outer { top: 33px; }
  .board-title--inner { top: 650px; }
  .page-label { position: absolute; font-size: 28px; }
  .spread {
    position: absolute; left: 194px; width: 721px;
    box-shadow: 0 8px 18px rgba(0,0,0,0.18);
  }
  .spread--outer { top: 197px; height: 361px; background: var(--brand-blue); }
  .spread--inner { top: 733px; height: 363px; background: var(--paper); }
  .spread__fold { position: absolute; left: 360px; top: 0; width: 1px; }
  .spread--outer .spread__fold { height: 100%; background: rgba(255,255,255,0.85); }
  .spread--inner .spread__fold { height: 349px; background: var(--fold); }
  .spread__band {
    position: absolute; left: 0; bottom: 0; width: 100%; height: 14px;
    background: var(--brand-blue);
  }
  .brand-name {
    position: absolute; font-size: 28px; letter-spacing: 0.5px; white-space: nowrap;
  }
  .brand-name--back { left: 0; width: 360px; top: 155px; text-align: center; color: var(--paper); }
  .brand-name--inside { right: 24px; top: 28px; font-size: 23px; color: var(--ink); }
  .event-name {
    position: absolute; left: 361px; width: 360px; top: 150px;
    text-align: center; font-size: 41px; color: var(--paper); letter-spacing: 0.5px;
  }
  .photo-area {
    position: absolute; left: 48px; top: 52px; width: 260px; height: 214px;
    border-radius: 10px;
    background: linear-gradient(180deg, #e3e3e0 0%, #9aa6ad 40%, #5f6e64 55%, #8a9298 70%, #a89a86 100%);
    border: 8px solid var(--brand-blue);
  }
  .ticket-note {
    position: absolute; left: 168px; top: 277px; width: 177px; height: 57px;
    border: 1.5px solid var(--brand-blue);
    text-align: center; color: var(--brand-blue); font-size: 17px; line-height: 22px; padding-top: 5px;
  }
  .ticket-note strong { font-family: "Ubuntu", sans-serif; font-weight: 700; font-size: 16px; }
  .date-box {
    position: absolute; left: 360px; top: 119px; width: 247px; height: 62px;
    background: var(--brand-blue); color: var(--paper);
    font-family: "Ubuntu", sans-serif; font-weight: 700; font-size: 22px; line-height: 24px;
    padding: 8px 0 0 38px;
  }
  .date-box__icon { position: absolute; left: 16px; top: 14px; }
  .venue { position: absolute; left: 380px; top: 204px; }
  .venue__pin { position: absolute; left: -4px; top: 1px; }
  .venue__name {
    padding-left: 14px; font-family: "Ubuntu", sans-serif; font-weight: 700;
    font-size: 16px; color: var(--brand-blue); letter-spacing: 0.4px;
  }
  .venue__address { padding-left: 14px; margin-top: 3px; font-size: 16px; color: var(--brand-grey); }
  .details { position: absolute; left: 376px; top: 274px; list-style: none; color: var(--brand-grey); font-size: 13.5px; line-height: 17px; }
  .details li { position: relative; padding-left: 14px; margin-bottom: 4px; }
  .details li::before {
    content: ""; position: absolute; left: 0; top: 3px;
    border-left: 10px solid var(--brand-blue);
    border-top: 5.5px solid transparent; border-bottom: 5.5px solid transparent;
  }
</style>
</head>
<body>
  <h2 class="board-title board-title--outer">OUTER PAGES</h2>
  <span class="page-label" style="left:194px; top:143px;">P4</span>
  <span class="page-label" style="left:877px; top:143px;">P1</span>

  <section class="spread spread--outer">
    <div class="brand-name brand-name--back">DER HELLE BOGEN</div>
    <div class="spread__fold"></div>
    <div class="event-name">ORTSABEND</div>
  </section>

  <h2 class="board-title board-title--inner">INNER PAGES</h2>

  <section class="spread spread--inner">
    <div class="photo-area" role="img" aria-label="Foto: Terrasse mit Sonnenschirm und gedeckten Tischen am See mit Segelbooten"></div>
    <div class="ticket-note">Diese Karte gilt als<br><strong>Eintrittskarte</strong></div>
    <div class="spread__fold"></div>

    <div class="brand-name brand-name--inside">DER HELLE BOGEN</div>

    <div class="date-box">
      <svg class="date-box__icon" width="16" height="16" viewBox="0 0 16 16" aria-hidden="true">
        <rect x="1" y="2.5" width="14" height="12.5" fill="none" stroke="#fff" stroke-width="1.3"/>
        <rect x="1" y="2.5" width="14" height="3" fill="#fff"/>
        <g fill="#fff"><rect x="3" y="7.5" width="2" height="2"/><rect x="7" y="7.5" width="2" height="2"/><rect x="11" y="7.5" width="2" height="2"/><rect x="3" y="11" width="2" height="2"/><rect x="7" y="11" width="2" height="2"/><rect x="11" y="11" width="2" height="2"/></g>
      </svg>
      Termin 03.07.2023<br>um 19 Uhr
    </div>

    <div class="venue">
      <svg class="venue__pin" width="12" height="16" viewBox="0 0 12 16" aria-hidden="true">
        <path d="M6 0.8A5.2 5.2 0 0 0 0.8 6c0 3.9 5.2 9.4 5.2 9.4s5.2-5.5 5.2-9.4A5.2 5.2 0 0 0 6 0.8z" fill="#176eb6"/>
        <circle cx="6" cy="6" r="2.2" fill="#fff"/>
      </svg>
      <div class="venue__name">KAIHALLE</div>
      <div class="venue__address">Lindenweg 52 &nbsp;|&nbsp; 90461 Nürnberg</div>
    </div>

    <ul class="details">
      <li>Anmeldung bis spätestens 23.06.2023<br>an events@heller-bogen.de</li>
      <li>Dresscode &nbsp;|&nbsp; Business Casual</li>
    </ul>

    <div class="spread__band"></div>
  </section>

  <span class="page-label" style="left:194px; top:1106px;">P2</span>
  <span class="page-label" style="left:877px; top:1106px;">P3</span>
</body>
</html>
```